Stationary Design

Harbor Stagecraft Collective, Inc
27410 Marlowe Blvd Ste 4, Lindenmoor, CA 90512
Office: 555-584-2760 Email: admin@hsccrew.example

Industry/Entity Type

Entertainment

Colors
0054AA
0677BA
7BADD7
CADEEF
E8F1F8

```html
<!DOCTYPE html>
<html lang="en">
<head>
<meta charset="utf-8">
<title>Harbor Stagecraft Collective — Stationery</title>
<link href="https://fonts.googleapis.com/css2?family=Cinzel:wght@500&family=Tinos&family=Lato:wght@400;700&family=Great+Vibes&display=swap" rel="stylesheet">
<style>
:root{
  --blue:#0054AA;
  --blue-mid:#0677BA;
  --blue-soft:#7BADD7;
  --blue-pale:#CADEEF;
  --blue-mist:#E8F1F8;
  --grey:#9a9a9a;
  --paper:#f1f1f1;
  --ink:#222;
  --bg:#b9b9bb;
}
*{box-sizing:border-box;margin:0;padding:0}
html,body{width:1200px;height:753px;overflow:hidden;background:var(--bg)}
.canvas{position:relative;width:1200px;height:753px;background:var(--bg)}
.piece{position:absolute;background:var(--paper);overflow:hidden;box-shadow:0 3px 6px rgba(0,0,0,.25)}
.swoosh{position:absolute;left:0;bottom:0;width:100%;display:block}
.brand{display:flex;align-items:center;gap:5px;font-family:'Cinzel',serif;font-weight:500;color:var(--blue);line-height:1.05}
.brand-dot{border-radius:50%;background:var(--blue);flex:none}
.company{font-family:'Cinzel',serif;font-weight:500;color:var(--blue);white-space:nowrap}
.contact{font-family:'Tinos',serif;color:var(--ink);list-style:none}
.contact li{display:flex;align-items:flex-start;gap:4px}
.contact svg{flex:none;fill:var(--blue);margin-top:1px}
.script{font-family:'Great Vibes',cursive;color:var(--blue)}

/* business card */
.card-front{left:35px;top:83px;width:162px;height:93px;text-align:center}
.card-front .brand{justify-content:center;font-size:7px;margin-top:16px}
.card-front .brand-dot{width:14px;height:14px}
.card-front .company{font-size:5px;margin-top:10px}
.card-front .contact{font-size:4.3px;margin-top:2px}
.card-front .contact li{justify-content:center}
.card-back{left:204px;top:83px;width:158px;height:93px;background:linear-gradient(180deg,#0b1a44 0%,#1b2f66 55%,#3a4c7a 75%,#12182e 100%)}
.card-back .brand{position:absolute;left:8px;top:8px;font-size:5px;color:#fff}
.card-back .brand-dot{width:8px;height:8px;background:#fff}

/* long card */
.slip{left:374px;top:91px;width:302px;height:83px}
.slip .company{position:absolute;left:20px;top:11px;font-size:8px}
.slip .contact{position:absolute;left:20px;top:22px;font-size:7px;line-height:1.25}
.slip .brand{position:absolute;right:20px;top:18px;width:88px;font-size:8px;flex-direction:column;text-align:center}
.slip .brand-dot{width:22px;height:22px}

/* letterhead */
.letter{left:34px;top:198px;width:328px;height:480px;font-family:'Lato',sans-serif;color:var(--ink)}
.letter .brand{position:absolute;left:25px;top:22px;width:120px;font-size:8.5px}
.letter .brand-dot{width:24px;height:24px}
.letter .head{position:absolute;left:189px;top:21px}
.letter .company{font-size:7px}
.letter .contact{font-size:6px;line-height:1.3;margin-top:3px}
.letter .body{position:absolute;left:25px;top:111px;width:280px;font-size:6.1px;line-height:1.2;text-align:justify}
.letter .body p{margin-bottom:7px}
.letter .salute{font-size:8px;font-weight:700;margin:9px 0 7px}
.letter .sign{font-size:16px;color:#333;margin-top:4px}

/* compliments slip */
.compliments{left:374px;top:198px;width:300px;height:155px}
.compliments .brand{position:absolute;left:16px;top:12px;width:80px;flex-direction:column;text-align:center;font-size:7.5px}
.compliments .brand-dot{width:26px;height:26px}
.compliments .title{position:absolute;right:18px;top:16px;font-size:17px}
.compliments .info{position:absolute;left:16px;top:71px}
.compliments .company{font-size:6.3px}
.compliments .contact{font-size:5.4px;line-height:1.3;margin-top:3px}

/* envelope back */
.env-back{left:374px;top:365px;width:300px;height:150px;background:#efefef}
.env-back .flap{position:absolute;left:0;top:0;width:300px;height:50px}
.env-back .brand{position:absolute;left:0;right:0;top:12px;justify-content:center;font-size:6.5px;color:#fff}
.env-back .brand-dot{width:16px;height:16px;background:#fff}

/* envelope front */
.env-front{left:374px;top:523px;width:300px;height:153px}
.env-front .brand{position:absolute;left:18px;top:14px;width:80px;flex-direction:column;text-align:center;font-size:7.5px}
.env-front .brand-dot{width:26px;height:26px}
.env-front .info{position:absolute;left:18px;top:76px}
.env-front .company{font-size:6px}
.env-front .contact{font-size:5.1px;line-height:1.3;margin-top:3px}
.env-front .window{position:absolute;right:17px;top:47px;width:73px;height:40px;border-radius:4px;background:linear-gradient(135deg,#d9d9d9,#b4b4b4)}

/* folder outside */
.folder-out{left:705px;top:55px;width:485px;height:305px;display:flex;box-shadow:0 3px 8px rgba(0,0,0,.3);background:none}
.folder-back{position:relative;width:242px;height:100%;background:var(--blue);color:#fff}
.folder-back .brand{position:absolute;left:24px;top:26px;font-size:10px;color:#fff}
.folder-back .brand-dot{width:22px;height:22px;background:#fff}
.folder-back .company{position:absolute;left:24px;bottom:42px;font-size:7.5px;color:#fff}
.folder-back .contact{position:absolute;left:24px;bottom:14px;font-size:6.5px;color:#fff;line-height:1.3}
.folder-back .contact svg{fill:#fff}
.folder-cover{position:relative;flex:1;background:var(--paper)}
.folder-cover .brand{position:absolute;left:0;right:0;top:95px;flex-direction:column;gap:8px;text-align:center;font-size:13px;color:var(--blue)}
.folder-cover .brand-dot{width:70px;height:70px;background:var(--blue-soft)}

/* folder front (light) */
.folder-front{left:710px;top:405px;width:140px;height:265px}
.folder-front .brand{position:absolute;left:12px;top:20px;font-size:9px;width:110px}
.folder-front .mark{position:absolute;left:30px;top:92px;width:80px;height:80px;border-radius:50%;background:var(--blue-pale)}
.folder-front .url{position:absolute;left:0;right:0;bottom:16px;text-align:center;font-family:'Lato',sans-serif;font-size:5px;color:var(--ink)}

/* folder inside */
.folder-in{left:920px;top:420px;width:262px;height:245px;background:#e4e4e4}
.mini{position:absolute;top:10px;width:110px;height:170px;background:#fafafa;font-family:'Lato',sans-serif;color:#555;padding:8px}
.mini .brand{font-size:3.6px}
.mini .brand-dot{width:7px;height:7px}
.mini p{font-size:3.4px;line-height:1.4;margin-top:4px}
.mini .lines{margin-top:4px;height:60px;background:repeating-linear-gradient(#fafafa 0 3px,#cfcfcf 3px 4px)}
.mini .sig{font-size:7px;color:#444;margin-top:4px}
.pocket{position:absolute;bottom:0;width:131px;height:60px;background:var(--blue)}
.pocket-left{left:0}
.pocket-right{right:0;clip-path:polygon(8% 0,100% 6%,100% 100%,0 100%)}
.mini-card{position:absolute;right:22px;bottom:30px;width:58px;height:30px;background:#fafafa;padding:4px;transform:rotate(2deg)}
.mini-card .brand{font-size:3px;justify-content:center}
.mini-card .brand-dot{width:5px;height:5px}
</style>
</head>
<body>
<svg width="0" height="0" style="position:absolute" aria-hidden="true">
  <defs>
    <symbol id="icon-phone" viewBox="0 0 10 10"><path d="M2 1h2l1 2.5-1.2.8a6 6 0 0 0 2 2l.8-1.2L9 6v2a1 1 0 0 1-1 1A8 8 0 0 1 1 2a1 1 0 0 1 1-1z"/></symbol>
    <symbol id="icon-mail" viewBox="0 0 10 10"><path d="M1 2.5h8v5H1z M1 2.5l4 3 4-3" /></symbol>
    <symbol id="icon-pin" viewBox="0 0 10 10"><path d="M5 .5a3.3 3.3 0 0 0-3.3 3.3C1.7 6.3 5 9.5 5 9.5s3.3-3.2 3.3-5.7A3.3 3.3 0 0 0 5 .5zm0 4.6a1.3 1.3 0 1 1 0-2.6 1.3 1.3 0 0 1 0 2.6z"/></symbol>
    <symbol id="swoosh" viewBox="0 0 300 40" preserveAspectRatio="none">
      <path d="M0 40 C90 24 190 12 300 7 L300 10 C190 14 90 27 0 40Z" fill="#9a9a9a"/>
      <path d="M0 40 C100 32 200 19 300 15 L300 40 Z" fill="#0054AA"/>
    </symbol>
  </defs>
</svg>

<main class="canvas">

  <section class="piece card-front">
    <div class="brand"><span class="brand-dot"></span>Harbor Stagecraft</div>
    <p class="company">Harbor Stagecraft Collective, Inc</p>
    <ul class="contact">
      <li><svg width="4" height="4"><use href="#icon-phone"/></svg>555-584-2760 &nbsp;<svg width="4" height="4"><use href="#icon-mail"/></svg>admin@hsccrew.example</li>
      <li>27410 Marlowe Blvd Ste 4, Lindenmoor, CA 90512</li>
    </ul>
    <svg class="swoosh" height="14"><use href="#swoosh"/></svg>
  </section>

  <section class="piece card-back" role="img" aria-label="Night city skyline photograph">
    <div class="brand"><span class="brand-dot"></span>Harbor Stagecraft</div>
  </section>

  <section class="piece slip">
    <p class="company">Harbor Stagecraft Collective, Inc</p>
    <ul class="contact">
      <li><svg width="6" height="6"><use href="#icon-phone"/></svg>555-584-2760</li>
      <li><svg width="6" height="6"><use href="#icon-mail"/></svg>admin@hsccrew.example</li>
      <li><svg width="6" height="6"><use href="#icon-pin"/></svg>27410 Marlowe Blvd Ste 4,<br>Lindenmoor, CA 90512</li>
    </ul>
    <div class="brand"><span class="brand-dot"></span>Harbor Stagecraft</div>
    <svg class="swoosh" width="302" height="22"><use href="#swoosh"/></svg>
  </section>

  <article class="piece letter">
    <div class="brand"><span class="brand-dot"></span>Harbor Stagecraft Collective</div>
    <div class="head">
      <p class="company">Harbor Stagecraft Collective, Inc</p>
      <ul class="contact">
        <li><svg width="5" height="5"><use href="#icon-phone"/></svg>555-584-2760</li>
        <li><svg width="5" height="5"><use href="#icon-mail"/></svg>admin@hsccrew.example</li>
        <li><svg width="5" height="5"><use href="#icon-pin"/></svg>27410 Marlowe Blvd Ste 4,<br>Lindenmoor, CA 90512</li>
      </ul>
    </div>
    <div class="body">
      <p style="margin-bottom:9px">Feb-03-2022</p>
      <p>Mr. Peter Lane<br>President</p>
      <p>Northway Corporation<br>123 Street Name, Suite# 10<br>City, State, 120023</p>
      <p class="salute">Dear Mr. Lane</p>
      <p>Lorem ipsum dolor sit amet, consectetur adipisicing elit, sed do eiusmod tempor incididunt ut labore et dolore magna aliqua. Ut enim ad minim veniam, quis nostrud exercitation ullamco laboris nisi ut aliquip ex ea commodo consequat. Duis aute irure dolor in reprehenderit in voluptate velit esse cillum dolore eu fugiat nulla pariatur.</p>
      <p>Lorem ipsum dolor sit amet, consectetur adipisicing elit, sed do eiusmod tempor incididunt ut labore et dolore magna aliqua. Ut enim ad minim veniam, quis nostrud exercitation ullamco laboris nisi ut aliquip ex ea commodo consequat. Duis aute irure dolor in reprehenderit in voluptate velit esse cillum dolore eu fugiat nulla pariatur.</p>
      <p>Lorem ipsum dolor sit amet, consectetur adipisicing elit, sed do eiusmod tempor incididunt ut labore et dolore magna aliqua. Ut enim ad minim veniam, quis nostrud exercitation ullamco laboris nisi ut aliquip ex ea commodo consequat.</p>
      <p>Excepteur sint occaecat cupidatat non proident, sunt in culpa qui officia deserunt mollit anim id est laborum. re et dolore magnam aliquam quaerat voluptatem.</p>
      <p style="margin-top:14px">Regards</p>
      <p class="script sign">Daniel Reyes</p>
    </div>
    <svg class="swoosh" width="328" height="28"><use href="#swoosh"/></svg>
  </article>

  <section class="piece compliments">
    <div class="brand"><span class="brand-dot"></span>Harbor Stagecraft</div>
    <p class="script title">With Compliments</p>
    <div class="info">
      <p class="company">Harbor Stagecraft Collective, Inc</p>
      <ul class="contact">
        <li><svg width="5" height="5"><use href="#icon-phone"/></svg>555-584-2760</li>
        <li><svg width="5" height="5"><use href="#icon-mail"/></svg>admin@hsccrew.example</li>
        <li><svg width="5" height="5"><use href="#icon-pin"/></svg>27410 Marlowe Blvd Ste 4,<br>Lindenmoor, CA 90512</li>
      </ul>
    </div>
    <svg class="swoosh" width="300" height="26"><use href="#swoosh"/></svg>
  </section>

  <section class="piece env-back">
    <svg class="flap" viewBox="0 0 300 50" preserveAspectRatio="none"><path d="M0 0H300V6C295 22 290 28 275 31L150 48 25 31C10 28 5 22 0 6Z" fill="#0054AA"/></svg>
    <div class="brand"><span class="brand-dot"></span>Harbor Stagecraft</div>
  </section>

  <section class="piece env-front">
    <div class="brand"><span class="brand-dot"></span>Harbor Stagecraft</div>
    <div class="info">
      <p class="company">Harbor Stagecraft Collective, Inc</p>
      <ul class="contact">
        <li><svg width="5" height="5"><use href="#icon-phone"/></svg>555-584-2760</li>
        <li><svg width="5" height="5"><use href="#icon-mail"/></svg>admin@hsccrew.example</li>
        <li><svg width="5" height="5"><use href="#icon-pin"/></svg>27410 Marlowe Blvd Ste 4,<br>Lindenmoor, CA 90512</li>
      </ul>
    </div>
    <div class="window"></div>
    <svg class="swoosh" width="300" height="26"><use href="#swoosh"/></svg>
  </section>

  <section class="piece folder-out">
    <div class="folder-back">
      <div class="brand"><span class="brand-dot"></span>Harbor Stagecraft</div>
      <p class="company">Harbor Stagecraft Collective, Inc</p>
      <ul class="contact">
        <li><svg width="6" height="6"><use href="#icon-phone"/></svg>555-584-2760 &nbsp;<svg width="6" height="6"><use href="#icon-mail"/></svg>admin@hsccrew.example</li>
        <li>27410 Marlowe Blvd Ste 4, Lindenmoor, CA 90512</li>
      </ul>
    </div>
    <div class="folder-cover">
      <div class="brand"><span class="brand-dot"></span>Harbor Stagecraft</div>
      <svg class="swoosh" width="243" height="40"><use href="#swoosh"/></svg>
    </div>
  </section>

  <section class="piece folder-front">
    <div class="brand">Harbor Stagecraft</div>
    <div class="mark"></div>
    <p class="url">www.hsccrew.example</p>
  </section>

  <section class="piece folder-in">
    <div class="mini" style="left:10px">
      <div class="brand"><span class="brand-dot"></span>Harbor Stagecraft</div>
      <p>Dear Mr. Lane</p>
      <p>Thank you for meeting our crew this week.</p>
      <div class="lines"></div>
      <p>Regards</p>
      <p class="script sig">Daniel Reyes</p>
    </div>
    <div class="mini" style="right:10px">
      <div class="brand"><span class="brand-dot"></span>Harbor Stagecraft</div>
      <p>Dear Mr. Lane</p>
      <p>Thank you for meeting our crew this week.</p>
      <div class="lines"></div>
      <p>Regards</p>
      <p class="script sig">Daniel Reyes</p>
    </div>
    <div class="pocket pocket-left"></div>
    <div class="pocket pocket-right"></div>
    <div class="mini-card"><div class="brand"><span class="brand-dot"></span>Harbor Stagecraft</div></div>
  </section>

</main>
</body>
</html>
```